Campaign: « ZUSAMMEN AKTIV », « Experience more together »

We would like to start a campaign for which we need a good visual appearance. So it's about creating a key visual that represents the activities around the campaign. The campaign « ZUSAMMEN AKTIV » in english « Experience more together » aims to make a valuable contribution to social integration and to counteract social isolation. More in the briefing.

Target Market(s)

Switzerland, Berne

Industry/Entity Type

Non Profit, NGO

Font styles to use
Sans Serif
Other font styles liked:
• Helvetica neue

Colors

Designer to choose colors to be used in the design.

```html
<!DOCTYPE html>
<html lang="en">
<head>
<meta charset="utf-8">
<title>Cheer Together – Key Visual</title>
<link rel="stylesheet" href="https://fonts.googleapis.com/css2?family=Archivo:wdth,wght@62..125,400..900&display=swap">
<style>
  :root {
    --red-deep: #7a0a1c;
    --red-mid: #a5101f;
    --red-bright: #d41a22;
    --white: #ffffff;
  }
  html, body {
    margin: 0;
    padding: 0;
    width: 1200px;
    height: 1200px;
    overflow: hidden;
    background: var(--red-deep);
  }
  .key-visual {
    position: relative;
    width: 1200px;
    height: 1200px;
    overflow: hidden;
    font-family: "Archivo", "Helvetica Neue", Arial, sans-serif;
    color: var(--white);
  }
  .photo-area {
    position: absolute;
    inset: 0;
    background:
      radial-gradient(ellipse 60% 55% at 55% 60%, var(--red-bright) 0%, rgba(212,26,34,0) 70%),
      radial-gradient(ellipse 50% 40% at 20% 55%, rgba(200,24,34,0.7) 0%, rgba(200,24,34,0) 70%),
      linear-gradient(180deg, #8c1427 0%, var(--red-mid) 45%, var(--red-deep) 100%);
  }
  .headline {
    position: absolute;
    left: 0;
    right: 0;
    top: 400px;
    margin: 0;
    text-align: center;
    font-weight: 900;
    font-stretch: 78%;
    font-size: 232px;
    line-height: 182px;
    letter-spacing: -5px;
  }
  .headline span { display: block; }
  .sender {
    position: absolute;
    left: 452px;
    top: 1039px;
    display: flex;
    align-items: center;
    gap: 20px;
  }
  .sender-dot {
    width: 72px;
    height: 72px;
    border-radius: 50%;
    background: var(--white);
  }
  .sender-name {
    font-weight: 600;
    font-size: 33px;
    line-height: 1;
    letter-spacing: 0.5px;
    text-transform: uppercase;
  }
</style>
</head>
<body>
  <main class="key-visual">
    <div class="photo-area" role="img" aria-label="Group of cheering football fans in red jerseys celebrating together on a coach bus, tinted red"></div>
    <h1 class="headline"><span>Cheer</span><span>Together</span></h1>
    <div class="sender">
      <div class="sender-dot"></div>
      <div class="sender-name">Zusammen Aktiv</div>
    </div>
  </main>
</body>
</html>
```